Loft Merchandise Email Marketing Template

ATTN DESIGNERS, UPDATED BRIEF! 3 JAN 2015.

- Email marketing template to promote our items.
- 7 items per email
- 1 main featured item on the top section - MUST BE ABOVE THE FOLD.
- every items with "call to action" buttonS (REQUEST SAMPLE button in grey colour and BUY NOW button in green colour).
- Red theme, but not too much.
- smart, simple AND MODERN feel
- our company logo attached.
- go to www.loftmerchandise.example.au to understand our company.
- FOLLOW THIS DESIGN / FEEL.
http://view.e.brightvisor.example.au/?j=abcd123456789012&m=ab1234567890123456&ls=ab1234567890123456789012&l=ab1234567890&s=ab123456789012345678&jb=ab12345678&ju=ab123456789012345678&r=0
- design submitted to be in EPS form, all layers neatly grouped and labelled.

Project Deadline Extended
Reason: Designs submitted are not satisfactory. We are still open for your submissions. Smart, simple, fun, creative feel desired. Red and grey colour theme. 7 items per email with 1 main featured item (larger display) at the top. Each items to have a "call to action" button. i.e. "REQUEST SAMPLE" button.

Target Market(s)

the target markets are marketing managers that are in charge of their companies marketing campaign, and the buying of promotional merchandises.

these guys ( the marketing manager, my target market) are busy, constantly under the pump, and results oriented.

Industry/Entity Type

Marketing

Font styles to use
Sans Serif

Colors
eb1f27

Requirements
Must have
• SMART, SMART AND SMART.
SIMPLE, CLEAN LOOK.
Should not have
• DULL, slow, wimpy look.

```html
<!DOCTYPE html>
<html lang="en">
<head>
<meta charset="utf-8">
<title>Loft Merchandise – Email Newsletter</title>
<link href="https://fonts.googleapis.com/css2?family=Arimo:ital,wght@0,400;0,700;1,400;1,700&display=swap" rel="stylesheet">
<style>
  :root {
    --red: #eb1f27;
    --grey-btn: #b9b9b9;
    --grey-btn-text: #3a3a3a;
    --green: #22ad39;
    --page-bg: #e0e0e0;
    --white: #ffffff;
    --ink: #111111;
    --rule: #dddddd;
    --legal-bg: #c9c9c9;
    --legal-ink: #444444;
    --bottom-bar: #3b3b3b;
  }
  * { box-sizing: border-box; margin: 0; padding: 0; }
  html, body { width: 673px; height: 1200px; overflow: hidden; }
  body {
    background: var(--page-bg);
    font-family: "Arimo", Arial, sans-serif;
    color: var(--ink);
  }
  .canvas { position: relative; width: 673px; height: 1200px; overflow: hidden; }
  .email {
    position: absolute; left: 84px; top: 0; width: 505px; height: 1200px;
    background: var(--white);
    box-shadow: 0 0 8px rgba(0,0,0,0.35);
  }
  .top-bar { position: absolute; left: 0; top: 0; width: 100%; height: 4px; background: var(--red); }
  .brand {
    position: absolute; left: 0; top: 4px; width: 100%; height: 78px;
    display: flex; align-items: center; justify-content: center;
    font-size: 26px; font-weight: 700; color: var(--red); letter-spacing: -0.3px;
  }
  .hero-photo {
    position: absolute; left: 0; top: 82px; width: 505px; height: 253px;
    background:
      radial-gradient(ellipse at 30% 35%, #2aa856 0 12%, transparent 30%),
      radial-gradient(ellipse at 55% 45%, #f2a431 0 20%, transparent 45%),
      radial-gradient(ellipse at 20% 60%, #e8788f 0 10%, transparent 28%),
      radial-gradient(ellipse at 85% 45%, #2630a8 0 15%, transparent 40%),
      radial-gradient(ellipse at 10% 85%, #2b35a8 0 12%, transparent 35%),
      linear-gradient(135deg, #c9ccd6, #9ea3b5);
  }
  .hero-offer {
    position: absolute; left: 103px; top: 251px; width: 300px; height: 109px;
    background: var(--red); border: 2px solid var(--red);
    box-shadow: inset 0 0 0 2px var(--white);
    text-align: center; color: var(--white); padding-top: 16px;
  }
  .hero-offer .title { font-size: 23.5px; font-weight: 700; line-height: 1; }
  .hero-offer .price { font-size: 12px; font-weight: 700; font-style: italic; margin-top: 5px; }
  .hero-offer .actions { display: flex; justify-content: center; gap: 28px; margin-top: 9px; }
  .btn {
    display: inline-flex; align-items: center; justify-content: center; gap: 3px;
    height: 25px; border-radius: 3px; font-size: 9.5px; font-weight: 700;
    text-decoration: none; text-transform: uppercase; white-space: nowrap;
    flex-shrink: 0;
  }
  .btn-sample { background: var(--grey-btn); color: var(--grey-btn-text); }
  .btn-buy { background: var(--green); color: var(--white); }
  .hero-offer .btn { font-size: 9px; }
  .hero-offer .btn-sample { width: 96px; gap: 2px; }
  .hero-offer .btn-buy { width: 117px; }
  .btn svg { display: block; flex-shrink: 0; }

  .product-grid {
    position: absolute; left: 0; top: 394px; width: 505px; height: 556px;
    display: grid; grid-template-columns: repeat(3, 1fr); grid-template-rows: repeat(2, 278px);
  }
  .product {
    position: relative; text-align: center;
    border-right: 1px solid var(--rule);
  }
  .product:nth-child(3n) { border-right: none; }
  .product:nth-child(-n+3) { border-bottom: 1px solid var(--rule); }
  .product-photo {
    position: absolute; left: 50%; top: 36px; width: 88px; height: 98px;
    transform: translateX(-50%); border-radius: 6px;
  }
  .product-name { position: absolute; left: 0; right: 0; top: 149px; font-size: 12.6px; font-weight: 700; white-space: nowrap; }
  .product-price { position: absolute; left: 0; right: 0; top: 168px; font-size: 8.5px; font-weight: 700; font-style: italic; color: var(--red); }
  .product .actions {
    position: absolute; left: 50%; top: 188px; transform: translateX(-50%);
    display: flex; flex-direction: column; gap: 4px; width: 118px;
  }
  .product .btn { width: 118px; }

  .contact-band {
    position: absolute; left: 0; top: 981px; width: 505px; height: 87px;
    background: var(--red); box-shadow: inset 0 0 0 3px var(--red), inset 0 0 0 5px var(--white);
    color: var(--white); text-align: center; font-size: 11px; font-weight: 700; line-height: 16px; padding-top: 15px;
  }
  .social { display: flex; justify-content: center; gap: 4px; margin-top: 5px; }
  .social span { width: 11px; height: 11px; background: var(--white); border-radius: 1px; }

  .legal {
    position: absolute; left: 0; top: 1068px; width: 505px; height: 126px;
    background: var(--legal-bg); color: var(--legal-ink); text-align: center; padding: 16px 18px 0;
  }
  .legal .terms { font-size: 8.6px; font-style: italic; line-height: 12px; }
  .legal .notice { font-size: 8.8px; font-weight: 700; margin-top: 14px; color: #333; }
  .legal .meta { font-size: 7.8px; font-weight: 700; margin-top: 5px; color: #333; }
  .bottom-bar { position: absolute; left: 0; top: 1194px; width: 505px; height: 6px; background: var(--bottom-bar); }
</style>
</head>
<body>
<div class="canvas">
  <div class="email">
    <div class="top-bar"></div>
    <header class="brand">Loft Merchandise</header>

    <section class="hero">
      <div class="hero-photo" role="img" aria-label="Photo of colourful silicone wristbands piled together"></div>
      <div class="hero-offer">
        <div class="title">SILICONE BRACELET</div>
        <div class="price">from $1.00 to $1.34 each</div>
        <div class="actions">
          <a class="btn btn-sample" href="#"><svg width="6" height="8" viewBox="0 0 6 8"><path d="M0 0L6 4L0 8Z" fill="#3a3a3a"/></svg>Request Sample</a>
          <a class="btn btn-buy" href="#"><svg width="13" height="11" viewBox="0 0 13 11"><path d="M0 1H2.5L4 7H11L12.5 2.5H3.2" fill="none" stroke="#fff" stroke-width="1.4"/><circle cx="5" cy="9.5" r="1.2" fill="#fff"/><circle cx="10" cy="9.5" r="1.2" fill="#fff"/></svg>Buy Now</a>
        </div>
      </div>
    </section>

    <section class="product-grid">
      <article class="product">
        <div class="product-photo" role="img" aria-label="Tote bags in many colours" style="background:linear-gradient(135deg,#e94b8a,#f6c21c 35%,#2a8f4f 60%,#2c3d9a)"></div>
        <h3 class="product-name">Avanti Tote Bag</h3>
        <p class="product-price">from $1.62 to $1.75 each</p>
        <div class="actions">
          <a class="btn btn-sample" href="#"><svg width="6" height="8" viewBox="0 0 6 8"><path d="M0 0L6 4L0 8Z" fill="#3a3a3a"/></svg>Request Sample</a>
          <a class="btn btn-buy" href="#"><svg width="13" height="11" viewBox="0 0 13 11"><path d="M0 1H2.5L4 7H11L12.5 2.5H3.2" fill="none" stroke="#fff" stroke-width="1.4"/><circle cx="5" cy="9.5" r="1.2" fill="#fff"/><circle cx="10" cy="9.5" r="1.2" fill="#fff"/></svg>Buy Now</a>
        </div>
      </article>
      <article class="product">
        <div class="product-photo" role="img" aria-label="Wristwatch with silver face and black strap" style="background:radial-gradient(circle at 50% 55%,#d8d8d8 0 28%,#2a2a2a 30% 45%,#f4f4f4 47%)"></div>
        <h3 class="product-name">Sunrise Watch</h3>
        <p class="product-price">from $7.75 to $9.07 each</p>
        <div class="actions">
          <a class="btn btn-sample" href="#"><svg width="6" height="8" viewBox="0 0 6 8"><path d="M0 0L6 4L0 8Z" fill="#3a3a3a"/></svg>Request Sample</a>
          <a class="btn btn-buy" href="#"><svg width="13" height="11" viewBox="0 0 13 11"><path d="M0 1H2.5L4 7H11L12.5 2.5H3.2" fill="none" stroke="#fff" stroke-width="1.4"/><circle cx="5" cy="9.5" r="1.2" fill="#fff"/><circle cx="10" cy="9.5" r="1.2" fill="#fff"/></svg>Buy Now</a>
        </div>
      </article>
      <article class="product">
        <div class="product-photo" role="img" aria-label="Bamboo phone stand holding a phone" style="background:linear-gradient(160deg,#4a4a4a 0 25%,#e0b98a 45%,#c9955e)"></div>
        <h3 class="product-name">Bamboo Phone Holder</h3>
        <p class="product-price">from $3.77 to $4.66 each</p>
        <div class="actions">
          <a class="btn btn-sample" href="#"><svg width="6" height="8" viewBox="0 0 6 8"><path d="M0 0L6 4L0 8Z" fill="#3a3a3a"/></svg>Request Sample</a>
          <a class="btn btn-buy" href="#"><svg width="13" height="11" viewBox="0 0 13 11"><path d="M0 1H2.5L4 7H11L12.5 2.5H3.2" fill="none" stroke="#fff" stroke-width="1.4"/><circle cx="5" cy="9.5" r="1.2" fill="#fff"/><circle cx="10" cy="9.5" r="1.2" fill="#fff"/></svg>Buy Now</a>
        </div>
      </article>
      <article class="product">
        <div class="product-photo" role="img" aria-label="Stainless steel travel coffee cup with black lid" style="background:linear-gradient(90deg,#f2f2f2 20%,#8c8c8c 30%,#e6e6e6 50%,#7a7a7a 70%,#f2f2f2 80%)"></div>
        <h3 class="product-name">Barista Coffee Cup</h3>
        <p class="product-price">from $5.09 to $5.43 each</p>
        <div class="actions">
          <a class="btn btn-sample" href="#"><svg width="6" height="8" viewBox="0 0 6 8"><path d="M0 0L6 4L0 8Z" fill="#3a3a3a"/></svg>Request Sample</a>
          <a class="btn btn-buy" href="#"><svg width="13" height="11" viewBox="0 0 13 11"><path d="M0 1H2.5L4 7H11L12.5 2.5H3.2" fill="none" stroke="#fff" stroke-width="1.4"/><circle cx="5" cy="9.5" r="1.2" fill="#fff"/><circle cx="10" cy="9.5" r="1.2" fill="#fff"/></svg>Buy Now</a>
        </div>
      </article>
      <article class="product">
        <div class="product-photo" role="img" aria-label="Power banks in silver, red, blue and black" style="background:linear-gradient(150deg,#c9c9c9 0 25%,#d7262c 40%,#2a8ad0 60%,#1e1e1e 80%)"></div>
        <h3 class="product-name">Voltcell Power Bank</h3>
        <p class="product-price">from $12.29 to $13.69 each</p>
        <div class="actions">
          <a class="btn btn-sample" href="#"><svg width="6" height="8" viewBox="0 0 6 8"><path d="M0 0L6 4L0 8Z" fill="#3a3a3a"/></svg>Request Sample</a>
          <a class="btn btn-buy" href="#"><svg width="13" height="11" viewBox="0 0 13 11"><path d="M0 1H2.5L4 7H11L12.5 2.5H3.2" fill="none" stroke="#fff" stroke-width="1.4"/><circle cx="5" cy="9.5" r="1.2" fill="#fff"/><circle cx="10" cy="9.5" r="1.2" fill="#fff"/></svg>Buy Now</a>
        </div>
      </article>
      <article class="product">
        <div class="product-photo" role="img" aria-label="Clear jar filled with coloured chocolate drops" style="background:radial-gradient(circle at 55% 60%,#e8b33a 0 12%,#c8362f 22%,#3a8d3e 34%,#2f5db0 46%,#e6e6e6 60%)"></div>
        <h3 class="product-name">Choc Drops in Container</h3>
        <p class="product-price">from $4.51 to $5.34 each</p>
        <div class="actions">
          <a class="btn btn-sample" href="#"><svg width="6" height="8" viewBox="0 0 6 8"><path d="M0 0L6 4L0 8Z" fill="#3a3a3a"/></svg>Request Sample</a>
          <a class="btn btn-buy" href="#"><svg width="13" height="11" viewBox="0 0 13 11"><path d="M0 1H2.5L4 7H11L12.5 2.5H3.2" fill="none" stroke="#fff" stroke-width="1.4"/><circle cx="5" cy="9.5" r="1.2" fill="#fff"/><circle cx="10" cy="9.5" r="1.2" fill="#fff"/></svg>Buy Now</a>
        </div>
      </article>
    </section>

    <footer>
      <div class="contact-band">
        <div>T: 1300 555 184 | F: 1300 555 534 | E: info@loftmerchandise.example.au</div>
        <div>Unit 4, 12 Station St, Kingsvale, Vic 3100</div>
        <div class="social" aria-label="Social links"><span></span><span></span><span></span><span></span></div>
      </div>
      <div class="legal">
        <p class="terms">TERMS &amp; CONDITIONS: Lorem ipsum dolor sit amet, consectetur adipiscing elit. Phasellus sit amet enim suscipit, suscipit magna vitae, accumsan neque. Praesent ac risus at dolor mattis pharetra. Curabitur efficitur, purus nec vehicula placerat, libero tortor consectetur quam, ut aliquet orci tortor ac est. Praesent nec tortor sit amet nulla tincidunt vestibulum nec vel urna. Donec congue, arcu a fermentum accumsan, massa lectus iaculis orci, at interdum erat risus at tellus. Etiam sodales, metus non faucibus luctus, ligula erat ultricies magna.</p>
        <p class="notice">You got this newsletter because subscriber@example.com is signed up for Loft Merchandise emails.</p>
        <p class="meta">©2014 Northvale. | Unsubscribe | Privacy Policy</p>
      </div>
      <div class="bottom-bar"></div>
    </footer>
  </div>
</div>
</body>
</html>
```